complete wordpress website template for the tuckwell company

I need a wordpress themed website designed for a new social enterprise who provide healthy catering/food supply to schools. It needs to be the FULL/COMPLETE wordpress theme! I want it to be simple, sleek, easy to use and SEO friendly.

I am going to leave the brief pretty open as I would like to see your ideas.

I am attaching a company logo and would like the design to incorporate the colours but not in an overpowering way. Keep it clean and crisp.

The mission of the company is to provide healthy catering and food supply to students in Irish schools with an emphasis on promoting increased consumption of fruit and veg so please keep this in mind. I would like space for images on main page and lower pages or maybe an image roll but very open here so will welcome your ideas
I want to be able to add tabs to the top level as we introduce new services.
Tabs should include
Home
About us
Our service (split into primary & post primary schools)
Resources again this will be split as above
Links
Contact us
Homepage should include a news section and links to social media being relatively prominent
Updates

Reason: I was requested to extend to allow time for more submissions

I have updated the brief for the project

Thanks

Rob

Reason: this is the last extension of the deadline.  WIll provide feedback on all designs over coming days

Target Market(s)

should appeal to principals, teachers and parents

Industry/Entity Type

Catering

Requirements
Must have
• incorporate logo and this should fit in with overall colour scheme and feel
links for facebook twitter etc must be relatively prominent
Feel like website not a blog
News page on front page possibly all pages
reflect the healthy eating ethos of the company
Nice to have
• contact form istock photos

```html
<!DOCTYPE html>
<html lang="en">
<head>
<meta charset="utf-8">
<title>The Tuckwell Company</title>
<link rel="stylesheet" href="https://fonts.googleapis.com/css2?family=Noto+Serif:wght@400;700&family=Roboto+Condensed:wght@400&family=PT+Sans:wght@400;700&display=swap">
<style>
:root{
  --lawn:#4f8f2a;
  --lawn-dark:#3e7a20;
  --frame:#e6e6e6;
  --paper:#ffffff;
  --sky:#22a6e0;
  --sky-dark:#1b8fc4;
  --orange:#f7941d;
  --red:#d62f3f;
  --ink:#333333;
  --body:#444444;
  --rule:#cccccc;
}
*{margin:0;padding:0;box-sizing:border-box}
html,body{width:1200px;height:1136px;overflow:hidden}
body{background:radial-gradient(circle at 50% 40%,var(--lawn) 0%,var(--lawn-dark) 100%);font-family:"PT Sans",sans-serif;color:var(--body);position:relative}
.page{position:absolute;left:136px;top:9px;width:928px;height:1094px;background:var(--frame);box-shadow:0 0 8px rgba(0,0,0,.4);overflow:hidden}
.sheet{position:absolute;left:10px;top:0;width:908px;height:1083px;background:var(--paper);overflow:hidden}
.header{position:absolute;left:0;top:0;width:908px;height:151px;background:linear-gradient(90deg,#fff 0%,#f3f2f5 50%,#f1f0f3 100%)}
.brand{position:absolute;left:17px;top:42px;display:flex;align-items:center;gap:10px}
.brand-name{font-family:"PT Sans",sans-serif;font-weight:700;font-size:26px;color:var(--sky);line-height:1.05;width:170px}
.brand-mark{width:56px;height:56px;border-radius:50%;background:#eeeeee}
.header-photo{position:absolute;right:0;top:5px;width:272px;height:146px;background:linear-gradient(180deg,#d9c3b1 0%,#c89b7e 55%,#e7e3d9 100%)}
.nav{position:absolute;left:0;top:151px;width:908px;height:42px;background:linear-gradient(var(--sky),var(--sky-dark));display:flex;padding-left:27px}
.nav a{font-family:"Roboto Condensed",sans-serif;font-size:16px;color:#fff;text-decoration:none;line-height:42px;margin-right:32px;position:relative}
.nav a.current::after{content:"";position:absolute;left:50%;bottom:0;margin-left:-5px;border:5px solid transparent;border-bottom-color:#fff}
.slider{position:absolute;left:1px;top:194px;width:906px;height:284px;background:radial-gradient(ellipse at 45% 55%,#d08a4a 0%,#c6773a 25%,#e8e2da 60%,#f4f2ef 100%)}
.slider svg{position:absolute;top:128px}
.slider .prev{left:26px}.slider .next{right:38px}
.slide-rule{position:absolute;left:0;top:479px;width:908px;height:6px;background:var(--orange)}
.main{position:absolute;left:18px;top:520px;width:570px}
h1{font-family:"Noto Serif",serif;font-weight:400;font-size:23px;color:var(--ink);letter-spacing:-.2px}
h1 strong{font-weight:700}
.main p{font-size:11.2px;line-height:13.6px;margin-top:8px;color:var(--body)}
.main p+p{margin-top:14px}
.btn{display:inline-block;background:var(--red);color:#fff;font-weight:700;font-size:11px;text-decoration:none;border:1px solid #b92332;box-shadow:inset 0 1px 0 rgba(255,255,255,.3)}
.btn-read{margin-top:18px;width:108px;height:28px;line-height:26px;padding-left:20px}
.services{position:absolute;left:19px;top:741px;width:566px;height:270px}
.services-head{height:66px;background:linear-gradient(#f5f5f5,#fff);padding:30px 14px 0}
.services-head h2{font-family:"Noto Serif",serif;font-weight:400;font-size:20px;color:var(--ink);padding-bottom:6px;border-bottom:1px dotted var(--rule)}
.services-photo{position:absolute;left:18px;top:92px;width:265px;height:146px;border:2px solid #e4e4e4;background:radial-gradient(ellipse at 40% 55%,#7ea83a 0%,#5a8a26 40%,#cfd8c0 100%)}
.services ul{position:absolute;left:310px;top:92px;list-style:none}
.services li{font-size:12px;font-weight:700;color:#333;letter-spacing:.3px;line-height:19.8px;padding-left:10px;position:relative}
.services li::before{content:"";position:absolute;left:0;top:8px;width:5px;height:5px;border-radius:50%;background:#333}
.divider{position:absolute;left:611px;top:506px;height:512px;border-left:1px dotted var(--rule)}
.side{position:absolute;left:627px;top:506px;width:266px}
.follow{display:flex;align-items:center;height:40px;padding-left:9px;white-space:nowrap}
.follow span{font-family:"Noto Serif",serif;font-size:17px;color:var(--ink);margin-right:auto;flex-shrink:0}
.social{flex-shrink:0;width:29px;height:35px;margin-left:7px;background:#e8dcc9;border:1px solid #d8cbb5;border-radius:2px}
.panel{margin-top:14px;background:linear-gradient(#f3f3f3,#fff 40px);padding:16px 9px 0}
.panel h3{font-family:"Noto Serif",serif;font-weight:400;font-size:20px;color:var(--ink)}
.email{display:block;margin-top:8px;width:245px;height:21px;border:1px solid #ccc;font-size:10px;color:#666;padding:3px 9px}
.btn-sub{display:block;margin:11px 0 0 157px;width:89px;height:20px;font-size:10px;line-height:18px;padding-left:18px;position:relative}
.btn-sub::before,.btn-more::before{content:"»";position:absolute;left:7px;font-size:13px;font-weight:400}
.news{margin-top:20px}
.news h3{padding-bottom:6px;border-bottom:1px dotted var(--rule)}
.news-item{padding:12px 0 10px;border-bottom:1px dotted var(--rule);font-size:9.8px;line-height:12.6px;color:#444}
.news-item:last-of-type{border-bottom:0}
.news-item a{display:block;margin-top:4px;font-weight:700;color:#222;text-decoration:none;font-size:10.5px}
.btn-more{position:relative;display:block;margin-top:10px;width:108px;height:28px;line-height:26px;padding-left:23px}
.footer{position:absolute;left:12px;top:1041px;width:884px;border-top:1px dotted var(--rule);text-align:center;font-size:10px;color:#555;padding-top:15px}
.footer a{color:#555;text-decoration:none}
.footer .sep{margin:0 9px}
</style>
</head>
<body>
<div class="page">
  <div class="sheet">
    <header class="header">
      <div class="brand"><span class="brand-name">The Tuckwell Company</span><span class="brand-mark"></span></div>
      <div class="header-photo" role="img" aria-label="Group of smiling school children giving a thumbs up"></div>
    </header>
    <nav class="nav">
      <a class="current" href="#">HOME</a><a href="#">ABOUT US</a><a href="#">OUR SERVICE</a><a href="#">RESOURCES</a><a href="#">LINKS</a><a href="#">CONTACT US</a>
    </nav>
    <div class="slider" role="img" aria-label="Close-up of sliced healthy wraps garnished with fresh coriander">
      <svg class="prev" width="12" height="22" viewBox="0 0 12 22"><path d="M10 2L2 11l8 9" fill="none" stroke="#fff" stroke-width="3"/></svg>
      <svg class="next" width="12" height="22" viewBox="0 0 12 22"><path d="M2 2l8 9-8 9" fill="none" stroke="#fff" stroke-width="3"/></svg>
    </div>
    <div class="slide-rule"></div>

    <section class="main">
      <h1>Welcome to <strong>The Tuckwell Company</strong></h1>
      <p>Lorem Ipsum is simply dummy text of the printing and typesetting industry. Lorem Ipsum has been the industry's standard dummy text ever since the 1500s, when an unknown printer took a galley of type and scrambled it to make a type specimen book. It has survived not only five centuries, but also the leap into electronic typesetting, remaining essentially unchanged. It was popularised in the 1960s with the release of Letraset sheets containing Lorem Ipsum passages, and more recently with desktop publishing software like Aldus PageMaker including versions of Lorem Ipsum.</p>
      <p>Lorem Ipsum has been the industry's standard dummy text ever since the 1500s, when an unknown printer took a galley of type and scrambled it to make a type specimen book.</p>
      <a class="btn btn-read" href="#">Read More...</a>
    </section>

    <section class="services">
      <div class="services-head"><h2>Our Services:</h2></div>
      <div class="services-photo" role="img" aria-label="Fresh green salad with croutons and tomatoes on a plate"></div>
      <ul>
        <li>Lorem Ipsum is simply dummy text.</li>
        <li>Lorem Ipsum is simply.</li>
        <li>Lorem Ipsum is dummy text.</li>
        <li>Lorem Ipsum text.</li>
        <li>Lorem Ipsum is simply dummy text.</li>
        <li>Lorem Ipsum is simply.</li>
        <li>Lorem Ipsum is dummy text.</li>
        <li>Lorem Ipsum text.</li>
      </ul>
    </section>

    <div class="divider"></div>

    <aside class="side">
      <div class="follow"><span>Follow us on</span>
        <a class="social" href="#" aria-label="Social network one"></a><a class="social" href="#" aria-label="Social network two"></a><a class="social" href="#" aria-label="Social network three"></a><a class="social" href="#" aria-label="News feed"></a>
      </div>
      <div class="panel">
        <h3>Newsletter</h3>
        <span class="email">Enter your email...</span>
        <a class="btn btn-sub" href="#">SUBSCRIBE</a>
      </div>
      <div class="panel news">
        <h3>News</h3>
        <div class="news-item">Lorem Ipsum is simply dummy text of the printing and typesetting industry. Lorem Ipsum has been the industry's standard dummy text ever since the 1500s, when an unknown printer took a galley...<a href="#">Read More...</a></div>
        <div class="news-item">Lorem Ipsum is simply dummy text of the printing and typesetting industry. Lorem Ipsum has been the industry's standard dummy text ever...<a href="#">Read More...</a></div>
        <div class="news-item">Lorem Ipsum is simply dummy text of the printing and typesetting industry. Lorem Ipsum has been the industry's standard...<a href="#">Read More...</a></div>
        <a class="btn btn-more" href="#">More News...</a>
      </div>
    </aside>

    <footer class="footer">©2011 TheTuckwellCompany<span class="sep">|</span><a href="#">Terms</a><span class="sep">|</span><a href="#">Privacy Policy</a></footer>
  </div>
</div>
</body>
</html>
```